Poster Design with Yoga Foam Roller Exercise Guide

Hi there!
We are looking for a poster design for our yoga foam roller product.
1. Foam roller.jpg shows our product. The poster is going to be wrapped around the roller
2. Poster dimensions: 42x28.5cm.
3. Design style matches our reference box.png and reference flat.png (colors, typefaces, overall look & feel)
4. Also check reference poster.jpg as a reference design for use of colors and overall look & feel
5. Written instructions are to be taken from written instructions.pdf
6. Illustrations are to be taken from illustrations.zip
7. Also use illustrations #2, 3 and 8 from girls.jpg, but add faces and change girl's hair (according to hair.jpg)
8. please see "jungle snugs. jpg" for the ambience of the colours (instead of green, please use a brown colour). the base colours must be plain, without grain.
9. Please also create a small label design (53x17mm, to be inserted into a socket in the foam roller, see label.jpg). Please use our logo (reference box/reference flat/logo.jpg) and/or „Velvet Orchard“ as text as you see fit.
Thank you very much, we are really excited about receiving your designs :)

```html
<!DOCTYPE html>
<html lang="de">
<head>
<meta charset="utf-8">
<title>Übungsbeispiele – Velvet Orchard Faszienrolle</title>
<link rel="stylesheet" href="https://fonts.googleapis.com/css2?family=Raleway:ital,wght@0,300;0,400;1,300&family=Hind:wght@400;600&display=swap">
<style>
  :root {
    --page: #ffffff;
    --cream: #f7efe3;
    --brown: #5c3d2c;
    --brown-dark: #6b4c3b;
    --accent: #a0725a;
    --text: #4a3a30;
    --line: #c9b6a3;
    --art-a: #e9dccb;
    --art-b: #d9c2a8;
    --label-ink: #f4ebe0;
  }
  * { margin: 0; padding: 0; box-sizing: border-box; }
  html, body { width: 1200px; height: 978px; overflow: hidden; background: var(--page); }
  body { position: relative; font-family: "Hind", sans-serif; color: var(--text); }

  .poster { position: absolute; left: 34px; top: 40px; width: 1126px; height: 763px; background: var(--cream); }
  .poster-title { position: absolute; left: 0; width: 100%; top: 42px; text-align: center;
    font-family: "Raleway", sans-serif; font-weight: 300; font-size: 44px; color: var(--brown); letter-spacing: 0.5px; }
  .poster-subtitle { position: absolute; left: 0; width: 100%; top: 98px; text-align: center;
    font-family: "Raleway", sans-serif; font-style: italic; font-weight: 300; font-size: 24px; color: var(--brown); }

  .exercise { position: absolute; width: 200px; }
  .art { position: absolute; border-radius: 40px; background: linear-gradient(90deg, var(--art-a), var(--art-b)); }
  .floor { position: absolute; height: 1px; background: var(--line); }
  .copy { position: absolute; width: 200px; font-size: 7.6px; line-height: 10px; }
  .lang { display: grid; grid-template-columns: 20px 1fr; margin-bottom: 6px; }
  .lang-tag { font-weight: 600; color: var(--accent); font-size: 8px; }
  .lang h3 { font-weight: 600; font-size: 8px; color: var(--accent); text-transform: uppercase; letter-spacing: 0.2px; }

  .side .copy { width: 130px; }
  .side .lang { display: block; }
  .side .lang-tag { display: block; }

  .brand { position: absolute; left: 0; width: 100%; top: 672px; text-align: center; }
  .brand-dot { position: absolute; left: 547px; top: 0; width: 32px; height: 32px; border-radius: 50%; background: var(--brown); }
  .brand-name { position: absolute; left: 0; width: 100%; top: 36px; font-family: "Raleway", sans-serif; font-weight: 400;
    font-size: 20px; letter-spacing: 6px; color: var(--brown); }

  .label { position: absolute; top: 847px; width: 277px; height: 89px; background: var(--brown-dark); color: var(--label-ink); }
  .label::before { content: ""; position: absolute; inset: 4px; border: 1px solid rgba(244,235,224,0.55); }
  .label-brand { position: absolute; left: 14px; top: 59px; width: 110px; text-align: center;
    font-family: "Raleway", sans-serif; font-size: 7px; letter-spacing: 1.8px; }
  .label-dot { position: absolute; left: 59px; top: 28px; width: 20px; height: 20px; border-radius: 50%; background: var(--label-ink); }
  .label-product { position: absolute; left: 134px; top: 30px; font-family: "Raleway", sans-serif; font-size: 21px; font-weight: 400; }
  .label-variant { position: absolute; left: 170px; top: 60px; font-family: "Raleway", sans-serif; font-style: italic; font-size: 8px; }
</style>
</head>
<body>
<main class="poster">
  <h1 class="poster-title">Übungsbeispiele</h1>
  <p class="poster-subtitle">Excercise Guide</p>

  <!-- Row 1 -->
  <section class="exercise" style="left:36px;top:170px">
    <div class="art" role="img" aria-label="Illustration: Mann liegt seitlich auf der Faszienrolle" style="left:4px;top:6px;width:190px;height:60px"></div>
    <div class="floor" style="left:0;top:70px;width:200px"></div>
    <div class="copy" style="top:86px">
      <div class="lang"><span class="lang-tag">DE</span><div><h3>Seitlicher Rücken</h3>Seitlich auf die Rolle legen, mit dem oberen Arm abstützen. Vom unteren Rücken bis zur Achsel vor- und zurückrollen.</div></div>
      <div class="lang"><span class="lang-tag">EN</span><div><h3>Lateral Back</h3>Lie down laterally on the foam roller, using the other arm as support. Then roll back and forth from the lower back to the armpit.</div></div>
    </div>
  </section>

  <section class="exercise" style="left:256px;top:170px">
    <div class="art" role="img" aria-label="Illustration: Frau bäuchlings auf der Rolle unter den Oberschenkeln" style="left:4px;top:10px;width:186px;height:56px"></div>
    <div class="floor" style="left:0;top:70px;width:200px"></div>
    <div class="copy" style="top:86px">
      <div class="lang"><span class="lang-tag">DE</span><div><h3>Vorderer Oberschenkel</h3>Bäuchlings auf die Rolle legen und unter die vorderen Oberschenkel positionieren. Mit den Armen abstützen. Gleichmäßig vor- und zurückrollen.</div></div>
      <div class="lang"><span class="lang-tag">EN</span><div><h3>Front of Upper Thighs</h3>Lying on the belly, position the roller under the quads. Use arms as support. Then roll back and forth, massaging the whole front of the upper thighs.</div></div>
    </div>
  </section>

  <section class="exercise" style="left:474px;top:170px">
    <div class="art" role="img" aria-label="Illustration: Frau liegt mit dem oberen Rücken auf der Rolle" style="left:8px;top:0;width:180px;height:66px"></div>
    <div class="floor" style="left:0;top:70px;width:200px"></div>
    <div class="copy" style="top:86px">
      <div class="lang"><span class="lang-tag">DE</span><div><h3>Oberer Rücken</h3>Mit dem oberen Rücken auf die Rolle legen. Vom Steißbein bis zur Schulter mit angewinkelten Beinen vor- und zurückrollen. Dabei den Bauch fest anspannen und bei Bedarf den Kopf abstützen.</div></div>
      <div class="lang"><span class="lang-tag">EN</span><div><h3>Upper Back</h3>Lie down with the upper back on the roller. With angled Legs, roll back and forth, keeping your stomach muscles under tension. Support your head with your hands if necessary.</div></div>
    </div>
  </section>

  <section class="exercise" style="left:692px;top:146px">
    <div class="art" role="img" aria-label="Illustration: Mann sitzt auf der Rolle und massiert das Gesäß" style="left:14px;top:0;width:150px;height:90px"></div>
    <div class="floor" style="left:0;top:94px;width:200px"></div>
    <div class="copy" style="top:110px">
      <div class="lang"><span class="lang-tag">DE</span><div><h3>Gesäß</h3>Auf die Rolle setzen, seitlich mit den Händen abstützen. Durch Bewegung der angewinkelten Beine Gesäß durch gleichmäßiges vor- und zurückrollen massieren.</div></div>
      <div class="lang"><span class="lang-tag">EN</span><div><h3>Buttock</h3>Sit on the roller, supporting yourself with your hands. By changing the angle of your legs, move back and forth on the roller, massaging your buttocks.</div></div>
    </div>
  </section>

  <section class="exercise side" style="left:900px;top:146px">
    <div class="art" role="img" aria-label="Illustration: Mann steht seitlich an der Wand, Rolle an der Schulter" style="left:0;top:0;width:66px;height:164px;border-radius:30px"></div>
    <div class="copy" style="left:78px;top:0">
      <div class="lang"><span class="lang-tag">DE</span><h3>Schultern (stehend)</h3>Seitlich an die Wand stellen, Leicht in die Knie gehen. Rolle zwischen Schultern und Wand einklemmen. Rolle auf- und abbewegen, indem Sie abwechselnd in die Knie gehen und die Beine strecken.</div>
      <div class="lang"><span class="lang-tag">EN</span><h3>Shoulders (standing)</h3>Stand sideways on a wall with slightly bended knees, roller between your shoulder and the wall. Roll up and down by alternately kneeling and stretching your legs.</div>
    </div>
  </section>

  <!-- Row 2 -->
  <section class="exercise" style="left:36px;top:406px">
    <div class="art" role="img" aria-label="Illustration: Mann sitzt, Rolle unter dem Oberschenkel" style="left:20px;top:0;width:160px;height:82px"></div>
    <div class="floor" style="left:0;top:86px;width:200px"></div>
    <div class="copy" style="top:102px">
      <div class="lang"><span class="lang-tag">DE</span><div><h3>Hinterer Oberschenkel</h3>Auf den Boden setzen, Rolle unter einen der Oberschenkel Legen. Mit beiden Armen abstützen, Gesäß anheben. Mit dem Oberschenkel gleichmäßiges vor- und zurückrollen. Danach Seite wechseln und wiederholen.</div></div>
      <div class="lang"><span class="lang-tag">EN</span><div><h3>Back of Upper Thighs</h3>Sit on the ground, place the roller under one of your thighs, supporting yourself with both arms. Raise your buttocks and roll back and forth over your thigh evenly. Switch side and repeat.</div></div>
    </div>
  </section>

  <section class="exercise" style="left:256px;top:406px">
    <div class="art" role="img" aria-label="Illustration: Mann sitzt, Rolle unter der Wade" style="left:20px;top:0;width:160px;height:82px"></div>
    <div class="floor" style="left:0;top:86px;width:200px"></div>
    <div class="copy" style="top:102px">
      <div class="lang"><span class="lang-tag">DE</span><div><h3>Waden</h3>Auf den Boden setzen, Rolle Liegt quer unter der Wade. Mit beiden Händen und dem freien Bein abstützen. Wade gleichmäßige vor- und zurückrollen. Bauch, Rücken und Po bleiben dabei angespannt.</div></div>
      <div class="lang"><span class="lang-tag">EN</span><div><h3>Calves</h3>Sit on the ground, roller placed under one calf. Support yourself with both hands and the other leg. Roll back and forth evenly while abdomen and back muscles remain tense.</div></div>
    </div>
  </section>

  <section class="exercise" style="left:474px;top:406px">
    <div class="art" role="img" aria-label="Illustration: Frau liegt seitlich, Rolle unter dem Oberschenkel" style="left:10px;top:12px;width:180px;height:70px"></div>
    <div class="floor" style="left:0;top:86px;width:200px"></div>
    <div class="copy" style="top:102px">
      <div class="lang"><span class="lang-tag">DE</span><div><h3>Seitlicher Oberschenkel</h3>Mit einem Oberschenkel seitlich auf die Rolle legen, mit Armen abstützen. Das andere Bein vor sich auf den Boden stellen. Oberschenkel von der Hüfte bis zum Knie vor- und zurückrollen. Danach Seite wechseln und wiederholen.</div></div>
      <div class="lang"><span class="lang-tag">EN</span><div><h3>Lateral Thighs</h3>Lie down laterally on the roller, supporting yourself with both arms. Position the other leg in front of you. Evenly move your thigh back and forth from hip to knee. Switch side and repeat.</div></div>
    </div>
  </section>

  <section class="exercise" style="left:692px;top:406px">
    <div class="art" role="img" aria-label="Illustration: Mann bäuchlings, Rolle an der Oberschenkelinnenseite" style="left:10px;top:28px;width:180px;height:54px"></div>
    <div class="floor" style="left:0;top:86px;width:200px"></div>
    <div class="copy" style="top:102px">
      <div class="lang"><span class="lang-tag">DE</span><div><h3>Oberschenkel - Innenseite</h3>Auf den Bauch Legen, mit abgewinkelten Armen abstützen. Ein Bein Richtung Schulter anwinkeln. Oberschenkelinnenseite auf die Rolle legen und vom Knie bis zum Becken vor- und zurückrollen.</div></div>
      <div class="lang"><span class="lang-tag">EN</span><div><h3>Inside of Upper Thighs</h3>Lay on the belly, supporting yourself with angled arms. Bend one leg toward the shoulder and place the inner thigh on the roller. Roll back and forth from knee to pelvis.</div></div>
    </div>
  </section>

  <section class="exercise side" style="left:900px;top:428px">
    <div class="art" role="img" aria-label="Illustration: Mann lehnt mit dem Rücken an der Wand, Rolle zwischen Rücken und Wand" style="left:0;top:0;width:66px;height:160px;border-radius:30px"></div>
    <div class="copy" style="left:78px;top:4px">
      <div class="lang"><span class="lang-tag">DE</span><h3>Oberer Rücken (stehend)</h3>Mit Leicht angewinkelten Knien vor eine Wand stellen, Rolle zwischen Rücken und Wand auf Höhe der Schulterblätter einklemmen. Rolle auf- und abbewegen, indem Sie abwechselnd in die Knie gehen und die Beine strecken.</div>
      <div class="lang"><span class="lang-tag">EN</span><h3>Upper Back (standing)</h3>Position yourself in front of a wall with your knees slightly bent, roller between your back and the wall at the level of the shoulder blades. Roll up and down by alternately kneeling and stretching your legs.</div>
    </div>
  </section>

  <footer class="brand">
    <span class="brand-dot"></span>
    <p class="brand-name">VELVET ORCHARD</p>
  </footer>
</main>

<aside class="label" style="left:319px">
  <span class="label-dot"></span>
  <p class="label-brand">VELVET ORCHARD</p>
  <p class="label-product">Faszienrolle</p>
  <p class="label-variant">schwarz/blau</p>
</aside>
<aside class="label" style="left:617px">
  <span class="label-dot"></span>
  <p class="label-brand">VELVET ORCHARD</p>
  <p class="label-product">Faszienrolle</p>
  <p class="label-variant">schwarz/blau</p>
</aside>
</body>
</html>
```